Etiketten-Design für Ober- & Rückseite eines Produktes
Zielgruppe
Bei diesem Produkt handelt es sich um eine hochwertige, vegane, essfertige Polenta in einer rechteckigen Tiefziehschale. Wir möchten ein Etikett auf der Oberseite sowie auf der Rückseite. Das Rückseiten Etikett enthält Zutaten, Nähwerttabelle, Rechtliche Hinweiße.
Bei diesem Produkt sehen wir den Kunden der eine schnelle, gesunde, nahrhafte, leicht zuzubereitende und schmackhafte Beilage zu vielen Speisen oder auch als Hauptgericht sucht.
Das gewünschte Format sowie weitere Elemente wie unser Firmenlogo und einen weiteren Eigenmarken Namen finden Sie in den Anhängen.
Aufgabenstellung
Da unserer Polenta Vegan ist sollte dies auch besonders Ausgelobt sein. Unter folgenden Produktnamen möchten wir Designs:
'Polenta Tessara Pura'
'Polenta Corvella La Scelta Dorata'
'Polenta Tessara, Gallo Verde'
Auf den Rückseitenetiketten sollte neben unserem Firmennamen und Logo, sich auch das Oberösterreiche Wappen finden.
Bei der Eigenmarke ' Feinwahl' nur den Schriftzug verwenden!

```html
<!DOCTYPE html>
<html lang="de">
<head>
<meta charset="utf-8">
<title>Polenta Etiketten – Oberseite</title>
<link rel="stylesheet" href="https://fonts.googleapis.com/css2?family=Kaushan+Script&family=Montserrat:wght@500;600;800&display=swap">
<style>
  :root {
    --bg: #b2b2b2;
    --leaf: #8db446;
    --tomato: #b12026;
    --paper: #ffffff;
    --ink: #161616;
    --brand-red: #c8242b;
  }
  html, body {
    margin: 0;
    padding: 0;
    width: 1200px;
    height: 3717px;
    overflow: hidden;
    background: var(--bg);
  }
  .sheet {
    position: relative;
    width: 1200px;
    height: 3717px;
  }
  .label {
    position: absolute;
    left: 267px;
    width: 672px;
    height: 746px;
    overflow: hidden;
    background: var(--paper);
  }
  .label--pura { top: 1153px; }
  .label--dorata { top: 1962px; }
  .label--gallo { top: 2770px; }
  .label__waves {
    position: absolute;
    inset: 0;
    width: 672px;
    height: 746px;
  }
  .wave-leaf { fill: var(--leaf); }
  .wave-tomato { fill: var(--tomato); }
  .label__vegan {
    position: absolute;
    top: 36px;
    right: 38px;
    margin: 0;
    font-family: "Montserrat", sans-serif;
    font-weight: 600;
    font-size: 31px;
    line-height: 1.2;
    letter-spacing: 0.5px;
    color: var(--paper);
  }
  .maker {
    position: absolute;
    top: 150px;
    left: 44px;
    display: flex;
    align-items: center;
    gap: 12px;
  }
  .maker__dot {
    width: 26px;
    height: 26px;
    border-radius: 50%;
    background: var(--brand-red);
  }
  .maker__name {
    font-family: "Montserrat", sans-serif;
    font-weight: 600;
    font-size: 29px;
    line-height: 1.2;
    color: var(--brand-red);
  }
  .product {
    position: absolute;
    left: 0;
    right: 0;
    top: 236px;
    text-align: center;
  }
  .product__name {
    margin: 0;
    font-family: "Kaushan Script", cursive;
    font-weight: 400;
    font-size: 124px;
    line-height: 1;
    color: var(--leaf);
    padding-left: 6px;
  }
  .product__variety {
    margin: 6px 0 0;
    font-family: "Montserrat", sans-serif;
    font-weight: 500;
    font-size: 34px;
    line-height: 42px;
    letter-spacing: 1.5px;
    color: var(--ink);
    text-transform: uppercase;
  }
  .house-brand {
    position: absolute;
    left: 0;
    right: 0;
    top: 526px;
    margin: 0;
    text-align: center;
    font-family: "Montserrat", sans-serif;
    font-weight: 800;
    font-size: 104px;
    line-height: 1.2;
    letter-spacing: -1px;
    color: var(--leaf);
  }
</style>
</head>
<body>
<main class="sheet">

  <section class="label label--pura">
    <svg class="label__waves" viewBox="0 0 448 497" preserveAspectRatio="none" aria-hidden="true">
      <path class="wave-leaf" d="M0,0 L448,0 L448,146 C380,82 250,30 0,18 Z"/>
      <path class="wave-tomato" d="M0,234 C90,300 210,338 290,336 C360,334 415,305 448,286 L448,497 L0,497 Z"/>
    </svg>
    <p class="label__vegan">VEGAN</p>
    <div class="maker"><span class="maker__dot"></span><span class="maker__name">Käserei Almbach</span></div>
    <div class="product">
      <h2 class="product__name">Polenta</h2>
      <p class="product__variety">Tessara<br>Pura</p>
    </div>
    <p class="house-brand">Feinwahl</p>
  </section>

  <section class="label label--dorata">
    <svg class="label__waves" viewBox="0 0 448 497" preserveAspectRatio="none" aria-hidden="true">
      <path class="wave-leaf" d="M0,0 L448,0 L448,146 C380,82 250,30 0,18 Z"/>
      <path class="wave-tomato" d="M0,234 C90,300 210,338 290,336 C360,334 415,305 448,286 L448,497 L0,497 Z"/>
    </svg>
    <p class="label__vegan">VEGAN</p>
    <div class="maker"><span class="maker__dot"></span><span class="maker__name">Käserei Almbach</span></div>
    <div class="product">
      <h2 class="product__name">Polenta</h2>
      <p class="product__variety">Corvella<br>La Scelta Dorata</p>
    </div>
    <p class="house-brand">Feinwahl</p>
  </section>

  <section class="label label--gallo">
    <svg class="label__waves" viewBox="0 0 448 497" preserveAspectRatio="none" aria-hidden="true">
      <path class="wave-leaf" d="M0,0 L448,0 L448,146 C380,82 250,30 0,18 Z"/>
      <path class="wave-tomato" d="M0,234 C90,300 210,338 290,336 C360,334 415,305 448,286 L448,497 L0,497 Z"/>
    </svg>
    <p class="label__vegan">VEGAN</p>
    <div class="maker"><span class="maker__dot"></span><span class="maker__name">Käserei Almbach</span></div>
    <div class="product">
      <h2 class="product__name">Polenta</h2>
      <p class="product__variety">Tessara<br>Gallo Verde</p>
    </div>
    <p class="house-brand">Feinwahl</p>
  </section>

</main>
</body>
</html>
```